Springtime Flyer Design

We are looking to redesign our flyer that we distribute to approximately 70,000 homes every spring. We would like it to emulate the other designs we recently had done on ArtBazaars which we have attached with a copy of our existing flyer. Thank you for looking at this project!

Target Market(s)

Residential homeowners

Industry/Entity Type

Landscaping

Font styles to use
Serif
Sans Serif

Requirements
Must have
• 1. Remove the TK Haulage logo on the bottom right
• 2. It should include all of the services offered but maybe in a nicer way
• 3. Should have our email and phone number on the flyer
• 4.Looking for a totally updated design that looks more contemporary and has a similar look to the attached files that we had done earlier on ArtBazaar.
• 5. This flyer is printed on white or yellow paper.
Nice to have
• Completely updated design

```html
<!DOCTYPE html>
<html lang="en">
<head>
<meta charset="utf-8">
<title>Maple Ridge Landscaping – Spring Flyer</title>
<link rel="stylesheet" href="https://fonts.googleapis.com/css2?family=Oswald:wght@300;400;500&family=Open+Sans:wght@400;600&display=swap">
<style>
  :root{
    --ink:#333333;
    --dark:#3a3a3a;
    --mid:#8c8c8c;
    --light:#d4d4d4;
    --paper:#ffffff;
  }
  *{margin:0;padding:0;box-sizing:border-box}
  html,body{width:750px;height:1200px;overflow:hidden;background:var(--paper)}
  .flyer{position:relative;width:750px;height:1200px;overflow:hidden;background:var(--paper);color:var(--ink);font-family:"Open Sans",sans-serif}

  .hero,.wave{position:absolute;left:0;top:0;width:750px;height:470px}

  .snapshot{position:absolute;border-radius:50%;border:6px solid var(--paper);box-shadow:0 0 0 3px var(--light)}
  .snapshot--garden{left:37px;top:316px;width:180px;height:180px;background:radial-gradient(circle at 40% 30%,#9cc7ef 0%,#e6b632 35%,#4f8f2a 65%,#2e5c1d 100%)}
  .snapshot--path{left:255px;top:277px;width:175px;height:175px;background:radial-gradient(circle at 50% 60%,#c9b89a 0%,#7bb33e 45%,#3d7424 80%,#d05a8a 100%)}

  .offer{position:absolute;left:490px;top:200px;width:210px;height:210px}
  .offer__text{position:absolute;inset:0;display:flex;flex-direction:column;align-items:center;justify-content:center;font-family:"Oswald",sans-serif;color:var(--dark);line-height:1}
  .offer__big{font-size:44px;font-weight:500}
  .offer__small{font-family:"Open Sans",sans-serif;font-size:19px;margin:6px 0 4px}
  .offer__only{font-size:38px;font-weight:500}

  .brand{position:absolute;left:420px;top:496px;width:330px;text-align:center;font-family:"Oswald",sans-serif;font-weight:300;font-size:30px;line-height:40px;letter-spacing:6px;color:var(--dark);text-transform:uppercase}

  .services-title{position:absolute;left:31px;top:535px;font-family:"Oswald",sans-serif;font-weight:500;color:var(--dark);line-height:1;text-transform:uppercase}
  .services-title__top{font-size:44px;display:block}
  .services-title__bottom{font-size:36px;display:block;margin-top:2px}
  .services-title__frame{position:absolute;left:197px;top:26px;width:86px;height:71px;border-top:2px solid var(--dark);border-right:2px solid var(--dark);border-bottom:2px solid var(--dark)}

  .service-list{position:absolute;left:36px;top:642px;list-style:none;font-family:"Oswald",sans-serif;font-weight:400;font-size:16px;color:var(--dark)}
  .service-list li{display:flex;align-items:center;height:29px}
  .service-list svg{width:14px;height:14px;margin-right:12px;flex:none}

  .tab{position:absolute;left:414px;top:574px;width:336px;height:203px;background:var(--dark);border-radius:24px 0 0 24px}
  .tab__row{position:absolute;left:0;display:flex;align-items:center;height:56px}
  .tab__row--one{top:8px}
  .tab__row--two{top:74px}
  .tab__row--three{top:138px}
  .tab__icon{width:40px;height:40px;border-radius:50%;background:var(--light);border:3px solid var(--paper);margin-left:4px;margin-right:18px;flex:none}
  .tab__label{font-family:"Oswald",sans-serif;font-weight:500;font-size:36px;color:var(--paper);text-transform:uppercase;letter-spacing:.5px}

  .divider{position:absolute;left:366px;top:790px;width:2px;height:325px;background:var(--dark)}
  .divider::after{content:"";position:absolute;left:-1px;top:94px;border-left:9px solid var(--dark);border-top:9px solid transparent;border-bottom:9px solid transparent}

  .about{position:absolute;left:390px;top:805px;width:337px;font-size:13.5px;line-height:21px;text-align:justify;color:var(--ink)}

  .contact-title{position:absolute;left:40px;top:916px;font-size:29px;line-height:40px;color:var(--dark)}
  .contact-title__frame{position:absolute;left:213px;top:922px;width:46px;height:36px;border-top:2px solid var(--dark);border-right:2px solid var(--dark);border-bottom:2px solid var(--dark)}
  .contact-list{position:absolute;left:34px;top:982px;list-style:none;color:var(--dark)}
  .contact-list li{display:flex;align-items:flex-start;margin-bottom:6px;font-size:18px;line-height:22px}
  .contact-list li.contact-list__address{font-size:14.5px;line-height:20px;margin-bottom:10px}
  .contact-list svg{width:16px;height:16px;margin:3px 10px 0 0;flex:none}

  .awards{position:absolute;left:390px;top:1030px;width:330px;height:84px}

  .cta{position:absolute;left:0;top:1135px;width:750px;height:65px;background:var(--dark);display:flex;align-items:center;justify-content:center;font-family:"Oswald",sans-serif;font-weight:500;font-size:34px;color:var(--paper);text-transform:uppercase;letter-spacing:.5px}
  .cta svg{width:34px;height:34px;margin-right:10px}
</style>
</head>
<body>
<main class="flyer">

  <svg class="hero" viewBox="0 0 750 470" role="img" aria-label="Photo of a landscaped front yard with a green lawn, flower beds and a house porch">
    <defs>
      <linearGradient id="heroGrad" x1="0" y1="0" x2="0" y2="1">
        <stop offset="0" stop-color="#c9c2b4"/>
        <stop offset=".32" stop-color="#6f8a4a"/>
        <stop offset=".55" stop-color="#4f8a2c"/>
        <stop offset="1" stop-color="#76b33c"/>
      </linearGradient>
      <radialGradient id="bedGrad" cx=".75" cy=".45" r=".45">
        <stop offset="0" stop-color="#c9508a" stop-opacity=".7"/>
        <stop offset=".6" stop-color="#a85a2e" stop-opacity=".35"/>
        <stop offset="1" stop-color="#a85a2e" stop-opacity="0"/>
      </radialGradient>
    </defs>
    <rect width="750" height="470" fill="url(#heroGrad)"/>
    <rect width="750" height="470" fill="url(#bedGrad)"/>
  </svg>

  <svg class="wave" viewBox="0 0 750 470" aria-hidden="true">
    <path d="M0 385 C150 360 330 335 470 338 C600 342 690 385 750 420" fill="none" stroke="#bdbdbd" stroke-width="14"/>
    <path d="M0 396 C160 372 340 350 480 352 C610 356 695 398 750 432 L750 470 L0 470 Z" fill="#ffffff"/>
  </svg>

  <div class="snapshot snapshot--garden" role="img" aria-label="Round photo of a garden path with autumn trees"></div>
  <div class="snapshot snapshot--path" role="img" aria-label="Round photo of a stone path winding through planted beds"></div>

  <div class="offer">
    <svg viewBox="0 0 210 210" width="210" height="210" aria-hidden="true">
      <circle cx="105" cy="105" r="96" fill="#d6d6d6"/>
      <circle cx="105" cy="105" r="99" fill="none" stroke="#d6d6d6" stroke-width="12" stroke-dasharray="9 6"/>
      <circle cx="105" cy="105" r="86" fill="none" stroke="#ffffff" stroke-width="1.5" stroke-dasharray="3 3"/>
    </svg>
    <div class="offer__text">
      <span class="offer__big">5% OFF</span>
      <span class="offer__small">New Customers</span>
      <span class="offer__only">ONLY</span>
    </div>
  </div>

  <div class="brand">Maple Ridge</div>

  <h2 class="services-title">
    <span class="services-title__top">Services</span>
    <span class="services-title__bottom">Offered Include</span>
    <span class="services-title__frame"></span>
  </h2>

  <ul class="service-list">
    <li><svg viewBox="0 0 14 14"><path d="M2 7 L6 11 L12 3" fill="none" stroke="#333" stroke-width="2"/></svg>Weekly lawn maintenancel</li>
    <li><svg viewBox="0 0 14 14"><path d="M2 7 L6 11 L12 3" fill="none" stroke="#333" stroke-width="2"/></svg>Spring / fall leaf clean-ups</li>
    <li><svg viewBox="0 0 14 14"><path d="M2 7 L6 11 L12 3" fill="none" stroke="#333" stroke-width="2"/></svg>Mulch / bark installation</li>
    <li><svg viewBox="0 0 14 14"><path d="M2 7 L6 11 L12 3" fill="none" stroke="#333" stroke-width="2"/></svg>shrub trimming</li>
    <li><svg viewBox="0 0 14 14"><path d="M2 7 L6 11 L12 3" fill="none" stroke="#333" stroke-width="2"/></svg>Lawn fertilization and weed control</li>
    <li><svg viewBox="0 0 14 14"><path d="M2 7 L6 11 L12 3" fill="none" stroke="#333" stroke-width="2"/></svg>Tree pruning or removal</li>
    <li><svg viewBox="0 0 14 14"><path d="M2 7 L6 11 L12 3" fill="none" stroke="#333" stroke-width="2"/></svg>Landscaping design and installation</li>
    <li><svg viewBox="0 0 14 14"><path d="M2 7 L6 11 L12 3" fill="none" stroke="#333" stroke-width="2"/></svg>Irrigation installation and service</li>
    <li><svg viewBox="0 0 14 14"><path d="M2 7 L6 11 L12 3" fill="none" stroke="#333" stroke-width="2"/></svg>Sod, hydro-seeding, and lawn renovation</li>
  </ul>

  <div class="tab">
    <div class="tab__row tab__row--one"><span class="tab__icon"></span><span class="tab__label">Landscaping</span></div>
    <div class="tab__row tab__row--two"><span class="tab__icon"></span><span class="tab__label">Lawncare</span></div>
    <div class="tab__row tab__row--three"><span class="tab__icon"></span><span class="tab__label">Leaf Clean-up</span></div>
  </div>

  <div class="divider"></div>
  <p class="about">Maple Ridge lawn Care has been servicing the Riverton area since 2005. Our commitment and dedication to quality has earned us a reputation we can be proud of. Using proper and well-maintained equipment on your project ensures quality and efficiency. Our goal is to exceed your expectations. We are looking forward to working with you on your next project. Contact us today to get started!</p>

  <div class="contact-title">Get In Touch</div>
  <div class="contact-title__frame"></div>
  <ul class="contact-list">
    <li class="contact-list__address"><svg viewBox="0 0 16 16"><path d="M8 1a5 5 0 0 0-5 5c0 4 5 9 5 9s5-5 5-9a5 5 0 0 0-5-5z" fill="none" stroke="#333" stroke-width="1.6"/><circle cx="8" cy="6" r="1.8" fill="#333"/></svg><span>742 Willow Bend Rd • Riverton,<br>MI 49000</span></li>
    <li><svg viewBox="0 0 16 16"><circle cx="8" cy="8" r="7" fill="none" stroke="#333" stroke-width="1.4"/><path d="M5 4.5l1.5 0 .8 2-1 .8a5 5 0 0 0 2.4 2.4l.8-1 2 .8v1.5c-3 .5-7-3.5-6.5-6.5z" fill="#333"/></svg>616-555-0142</li>
    <li><svg viewBox="0 0 16 16"><circle cx="8" cy="8" r="7.5" fill="#333"/><rect x="4" y="5" width="8" height="6" fill="#fff"/><path d="M4 5l4 3 4-3" fill="none" stroke="#333" stroke-width="1"/></svg>hello@mapleridgeyard.com</li>
    <li><svg viewBox="0 0 16 16"><circle cx="8" cy="8" r="7" fill="none" stroke="#333" stroke-width="1.4"/><ellipse cx="8" cy="8" rx="3" ry="7" fill="none" stroke="#333" stroke-width="1"/><path d="M1 8h14" stroke="#333" stroke-width="1"/></svg>www.mapleridgeyard.com</li>
  </ul>

  <svg class="awards" viewBox="0 0 330 84" aria-hidden="true">
    <circle cx="45" cy="34" r="28" fill="#bdbdbd" stroke="#8c8c8c" stroke-width="3"/>
    <path d="M32 57 L28 80 L40 72 L45 80 L45 60 Z M58 57 L62 80 L50 72 L45 80 L45 60 Z" fill="#8c8c8c"/>
    <path d="M118 8 h44 v38 q0 22 -22 30 q-22 -8 -22 -30 z" fill="#9e9e9e"/>
    <path d="M198 14 q22 -12 44 0 v30 q0 20 -22 28 q-22 -8 -22 -28 z" fill="#c4c4c4"/>
    <path d="M272 4 h40 v48 l-20 22 l-20 -22 z" fill="#8c8c8c"/>
  </svg>

  <div class="cta">
    <svg viewBox="0 0 34 34" aria-hidden="true"><circle cx="17" cy="17" r="15" fill="none" stroke="#fff" stroke-width="2"/><path d="M11 9h3.5l1.8 4.5-2.2 1.7a11 11 0 0 0 5.7 5.7l1.7-2.2 4.5 1.8V24c-7 1-16-8-15-15z" fill="#fff"/></svg>
    555-0142 Today for a free proposal
  </div>

</main>
</body>
</html>
```